WPF Application Design

I require a design for a WPF application. I have the screenshots which needs to be redesigned for WPF application. Screens have different standard controls used, designer should suggest best placement and styling for the screens.

```html
<!DOCTYPE html>
<html lang="en">
<head>
<meta charset="utf-8">
<title>Course Template</title>
<link rel="stylesheet" href="https://fonts.googleapis.com/css2?family=Source+Sans+3:wght@300;400;600&display=swap">
<style>
  :root {
    --canvas: #ffffff;
    --title-blue: #1f74bd;
    --home-blue: #2aa6e0;
    --accent-cyan: #2aa8e0;
    --link-blue: #2a7cc0;
    --workspace: #e9e9e9;
    --panel: #ffffff;
    --section: #ededed;
    --header-row: #e6e6e6;
    --border: #c9c9c9;
    --text: #4a4a4a;
    --muted: #bdbdbd;
    --disabled: #c8c8c8;
    --dot-root: #1e6fb8;
    --dot-level1: #2aa8e0;
    --dot-level2: #e0245e;
    --dot-level3: #8dc63f;
    --bullet: #6f6f6f;
    --radio-on: #1f74bd;
  }
  * { box-sizing: border-box; margin: 0; padding: 0; }
  html, body { width: 1200px; height: 900px; overflow: hidden; background: var(--canvas); }
  body { font-family: "Source Sans 3", sans-serif; color: var(--text); position: relative; }

  .window {
    position: absolute; left: 89px; top: 111px; width: 1020px; height: 647px;
    background: var(--workspace);
    box-shadow: 0 1px 5px rgba(0,0,0,0.35);
  }
  .title-bar { position: absolute; left: 0; top: 0; width: 100%; height: 64px; background: var(--title-blue); }
  .home-button { position: absolute; left: 10px; top: 7px; width: 65px; height: 52px; background: var(--home-blue); display: flex; align-items: center; justify-content: center; }
  .settings-button { position: absolute; left: 81px; top: 14px; width: 36px; height: 36px; }
  .window-title { position: absolute; left: 381px; width: 200px; top: 0; line-height: 64px; text-align: center; color: #fff; font-weight: 300; font-size: 29px; }
  .window-controls { position: absolute; right: 12px; top: 12px; display: flex; gap: 19px; }
  .window-controls svg { width: 20px; height: 20px; }

  .main-nav { position: absolute; left: 0; top: 64px; width: 100%; height: 73px; background: var(--panel); }
  .nav-tab { position: absolute; top: 9px; width: 131px; height: 56px; display: flex; align-items: center; justify-content: center; text-align: center; font-size: 17.5px; line-height: 22px; color: var(--link-blue); font-weight: 300; }
  .nav-tab.is-active { border: 1px solid var(--link-blue); }
  .nav-rule { position: absolute; left: 0; top: 137px; width: 100%; height: 7px; background: var(--accent-cyan); }

  .group-tree { position: absolute; left: 2px; top: 153px; width: 288px; height: 486px; background: var(--panel); padding-top: 21px; list-style: none; }
  .group-tree li { height: 23.4px; display: flex; align-items: center; font-size: 17px; font-weight: 300; color: var(--text); }
  .group-tree li::before { content: ""; width: 15px; height: 15px; border-radius: 50%; margin-right: 9px; flex: none; }
  .level-0 { padding-left: 13px; } .level-0::before { background: var(--dot-root); }
  .level-1 { padding-left: 60px; } .level-1::before { background: var(--dot-level1); }
  .level-2 { padding-left: 107px; } .level-2::before { background: var(--dot-level2); }
  .level-3 { padding-left: 154px; } .level-3::before { background: var(--dot-level3); }

  .template-manager { position: absolute; left: 299px; top: 153px; width: 721px; height: 219px; background: var(--panel); }
  .panel-heading { position: absolute; left: 0; width: 100%; top: 8px; text-align: center; font-size: 17px; font-weight: 400; color: var(--link-blue); }
  .search-field { position: absolute; left: 9px; top: 35px; width: 704px; height: 26px; border: 1px solid var(--border); text-align: right; padding-right: 6px; font-size: 16.5px; line-height: 24px; color: var(--muted); font-weight: 300; }
  .template-table { position: absolute; left: 9px; top: 81px; width: 704px; border-collapse: collapse; font-size: 13px; }
  .template-table th { background: var(--header-row); font-weight: 400; height: 25px; text-align: center; width: 117px; }
  .template-table td { height: 26px; text-align: center; }

  .template-details { position: absolute; left: 299px; top: 381px; width: 721px; height: 259px; background: var(--panel); }
  .detail-tab { position: absolute; top: 7px; width: 82px; height: 38px; display: flex; align-items: center; justify-content: center; text-align: center; font-size: 13px; line-height: 15px; color: var(--link-blue); font-weight: 300; }
  .detail-tab.is-active { border: 1px solid var(--link-blue); }
  .detail-tab.is-disabled { color: var(--disabled); }
  .detail-tabs-rule { position: absolute; left: 14px; right: 14px; top: 53px; height: 1px; background: #ececec; }

  .section { position: absolute; left: 25px; width: 675px; background: var(--section); }
  .section-title { display: flex; align-items: center; height: 29px; padding-left: 16px; font-size: 17.5px; font-weight: 300; color: var(--text); }
  .section-title::before { content: ""; width: 15px; height: 15px; border-radius: 50%; background: var(--bullet); margin-right: 10px; }
  .section.price { top: 58px; height: 29px; }
  .section.discount { top: 91px; height: 160px; }

  .field { position: absolute; transform: translate(-50%, -50%); font-size: 13px; white-space: nowrap; }
  .field.label-strong { font-weight: 600; }
  .number-input { position: absolute; left: 218px; width: 57px; height: 23px; border: 1px solid #9a9a9a; background: #fff; font-size: 13px; text-align: center; line-height: 21px; transform: translateY(-50%); }
  .radio { position: absolute; width: 26px; height: 26px; border-radius: 50%; border: 1px solid #9a9a9a; background: #fff; transform: translate(-50%, -50%); }
  .radio.is-checked::after { content: ""; position: absolute; left: 50%; top: 50%; width: 15px; height: 15px; border-radius: 50%; background: var(--radio-on); transform: translate(-50%, -50%); }
  .checkbox { position: absolute; left: 452px; width: 25px; height: 25px; border: 1px solid #9a9a9a; background: #fff; transform: translateY(-50%); }
</style>
</head>
<body>
<div class="window">
  <header class="title-bar">
    <div class="home-button">
      <svg width="40" height="36" viewBox="0 0 40 36" fill="none" stroke="#fff" stroke-width="2">
        <path d="M3 16 L20 3 L37 16"/>
        <rect x="7" y="15" width="26" height="19"/>
        <rect x="16" y="22" width="8" height="12"/>
      </svg>
    </div>
    <svg class="settings-button" viewBox="0 0 36 36" fill="none" stroke="#fff" stroke-width="1.8">
      <path d="M15.5 3h5l.8 4.2 2.9 1.2 3.5-2.4 3.5 3.5-2.4 3.5 1.2 2.9 4.2.8v5l-4.2.8-1.2 2.9 2.4 3.5-3.5 3.5-3.5-2.4-2.9 1.2-.8 4.2h-5l-.8-4.2-2.9-1.2-3.5 2.4-3.5-3.5 2.4-3.5-1.2-2.9L3 20.5v-5l4.2-.8 1.2-2.9-2.4-3.5 3.5-3.5 3.5 2.4 2.9-1.2z"/>
      <circle cx="18" cy="18" r="6"/>
    </svg>
    <h1 class="window-title">Course Template</h1>
    <div class="window-controls">
      <svg viewBox="0 0 20 20" stroke="#fff" stroke-width="2"><path d="M4 8h12"/></svg>
      <svg viewBox="0 0 20 20" stroke="#fff" stroke-width="2" fill="none"><rect x="4" y="4" width="12" height="12"/></svg>
      <svg viewBox="0 0 20 20" stroke="#fff" stroke-width="2"><path d="M5 5l10 10M15 5L5 15"/></svg>
    </div>
  </header>

  <nav class="main-nav">
    <div class="nav-tab is-active" style="left:6px">Course Hierachy<br>Manager</div>
    <div class="nav-tab" style="left:137px">Course<br>Group</div>
    <div class="nav-tab" style="left:268px">Course<br>Type</div>
    <div class="nav-tab" style="left:400px">Course<br>Step</div>
    <div class="nav-tab" style="left:531px">Course<br>Template</div>
  </nav>
  <div class="nav-rule"></div>

  <ul class="group-tree">
    <li class="level-0">All Course Groups</li>
    <li class="level-1">Group Text</li>
    <li class="level-1">Group Text</li>
    <li class="level-1">Group Text</li>
    <li class="level-1">Group Text</li>
    <li class="level-2">Group Text</li>
    <li class="level-2">Group Text</li>
    <li class="level-3">Group Text</li>
    <li class="level-3">Group Text</li>
    <li class="level-1">Group Text</li>
    <li class="level-1">Group Text</li>
    <li class="level-1">Group Text</li>
    <li class="level-1">Group Text</li>
    <li class="level-1">Group Text</li>
    <li class="level-1">Group Text</li>
    <li class="level-1">Group Text</li>
    <li class="level-2">Group Text</li>
    <li class="level-3">Group Text</li>
  </ul>

  <section class="template-manager">
    <h2 class="panel-heading">Course Template Manager</h2>
    <div class="search-field">Type text to search</div>
    <table class="template-table">
      <thead>
        <tr><th>Template Name</th><th>Template Name</th><th>Template Name</th><th>Template Name</th><th>Template Name</th><th>Template Name</th></tr>
      </thead>
      <tbody>
        <tr><td>1234</td><td>123456</td><td>A1</td><td>1234</td><td>123456</td><td>A1</td></tr>
        <tr><td>5678</td><td>654321</td><td>B2</td><td>5678</td><td>654321</td><td>B2</td></tr>
      </tbody>
    </table>
  </section>

  <section class="template-details">
    <div class="detail-tab is-active" style="left:20px">Template<br>Type</div>
    <div class="detail-tab" style="left:122px">General</div>
    <div class="detail-tab" style="left:224px">Finance</div>
    <div class="detail-tab is-disabled" style="left:326px">Preliminary<br>Course</div>
    <div class="detail-tab is-disabled" style="left:428px">Package</div>
    <div class="detail-tab" style="left:530px">Learning<br>Goals</div>
    <div class="detail-tab" style="left:632px">Remark</div>
    <div class="detail-tabs-rule"></div>

    <div class="section price"><div class="section-title">Price and Payment</div></div>

    <div class="section discount">
      <div class="section-title">Discount</div>
      <span class="field label-strong" style="left:539px;top:40px">Changeable</span>
      <span class="field label-strong" style="left:325px;top:64px">Discount In</span>
      <span class="field label-strong" style="left:527px;top:64px">Yes</span>
      <span class="field label-strong" style="left:575px;top:64px">No</span>

      <span class="field" style="left:141px;top:100px">Few Discount</span>
      <div class="number-input" style="top:100px">0</div>
      <span class="radio" style="left:316px;top:100px"></span>
      <span class="field" style="left:343px;top:100px">%</span>
      <span class="radio" style="left:375px;top:100px"></span>
      <span class="field" style="left:414px;top:100px">Actual</span>
      <span class="checkbox" style="top:100px"></span>
      <span class="radio" style="left:530px;top:100px"></span>
      <span class="radio is-checked" style="left:580px;top:100px"></span>

      <span class="field" style="left:141px;top:135px">Few Discount</span>
      <div class="number-input" style="top:135px">0</div>
      <span class="radio" style="left:316px;top:135px"></span>
      <span class="field" style="left:343px;top:135px">%</span>
      <span class="radio" style="left:375px;top:135px"></span>
      <span class="field" style="left:414px;top:135px">Actual</span>
      <span class="checkbox" style="top:135px"></span>
      <span class="radio" style="left:530px;top:135px"></span>
      <span class="radio is-checked" style="left:580px;top:135px"></span>
    </div>
  </section>
</div>
</body>
</html>
```